corwin's pastel

We are a family business based in sydney introducing a common brazilian street food into sydney cafes and restaurants.
what we provide are pastels which is a thinly crust pie with assorted fillings
we mainly focus on supplying cafes and restaurants but we do sell privately.
We have had a few cafes ask to stock our cards due to customer request. except we don't have any!! hence why we need you. : )
I have attached an image of our pastels which is just to give you an idea of what they look like.
Updates
I have just seen all the designs and am impressed by some of your work. I will have to sit with my parter later today and will hopefully have some more constructive feedback and a decision soon.
Hello designers,
Hello designers,
Target Market(s)
cafe's and restaurants
Industry/Entity Type
Business
Contact Information for Business Card
Corwin's pastel
joaquim 0468217094
corwinspastel@fernmail.example

```html
<!DOCTYPE html>
<html lang="en">
<head>
<meta charset="utf-8">
<title>Corwin's pastel – business card options</title>
<link rel="stylesheet" href="https://fonts.googleapis.com/css2?family=Caveat+Brush&family=Delius&display=swap">
<style>
  :root {
    --sheet: #ffffff;
    --sheet-edge: #d9d9d9;
    --label: #222222;
    --ink: #2b1d12;
    --lime: #8cc63f;
    --lime-deep: #5fae2e;
    --leaf: #2f9a3a;
    --orange: #f7941d;
    --orange-deep: #f15a24;
    --sun: #fff200;
    --cream: #fffde8;
    --pastry: #d89a55;
    --pastry-light: #f3d3a0;
  }
  html, body {
    margin: 0;
    padding: 0;
    width: 1200px;
    height: 912px;
    overflow: hidden;
    background: var(--sheet);
  }
  .sheet {
    position: relative;
    width: 1198px;
    height: 910px;
    border: 1px solid var(--sheet-edge);
    background: var(--sheet);
  }
  .option-number {
    position: absolute;
    font-family: Arial, Helvetica, sans-serif;
    font-size: 34px;
    color: var(--label);
  }
  .option-number--one { left: 42px; top: 136px; }
  .option-number--two { left: 608px; top: 120px; }

  .card {
    position: absolute;
    width: 418px;
    height: 700px;
    overflow: hidden;
    box-shadow: 2px 3px 8px rgba(0,0,0,0.25);
  }
  .card--green { left: 110px; top: 100px; }
  .card--orange { left: 667px; top: 98px; }
  .card__art { position: absolute; inset: 0; }

  .pastel-photo {
    position: absolute;
    border-radius: 48% 48% 30% 30% / 60% 60% 30% 30%;
    background: radial-gradient(ellipse at 50% 45%, var(--pastry-light) 0%, var(--pastry) 65%, #b8702e 100%);
  }
  .card--green .pastel-photo { left: 65px; top: 75px; width: 295px; height: 255px; }
  .card--orange .pastel-photo { left: 63px; top: 420px; width: 305px; height: 278px; }

  .brand-name {
    position: absolute;
    left: 0; right: 0;
    margin: 0;
    text-align: center;
    font-family: "Caveat Brush", cursive;
    font-weight: 400;
    font-size: 66px;
    color: var(--ink);
    line-height: 1;
  }
  .phone {
    position: absolute;
    left: 0; right: 0;
    display: flex;
    justify-content: center;
    align-items: center;
    gap: 4px;
    font-family: "Caveat Brush", cursive;
    font-size: 44px;
    line-height: 1;
  }
  .phone svg { width: 30px; height: 30px; }
  .email {
    position: absolute;
    left: 0; right: 0;
    text-align: center;
    font-family: "Delius", cursive;
    font-size: 27px;
    color: var(--ink);
  }

  .card--green .brand-name { top: 410px; text-shadow: 2px 2px 0 var(--orange); }
  .card--green .phone { top: 532px; color: var(--orange); }
  .card--green .phone svg { fill: var(--orange-deep); }
  .card--green .email { top: 612px; }

  .card--orange .brand-name { top: 68px; }
  .card--orange .phone { top: 180px; color: var(--ink); }
  .card--orange .phone svg { fill: var(--ink); }
  .card--orange .email { top: 260px; }
</style>
</head>
<body>
<main class="sheet">
  <span class="option-number option-number--one">1</span>
  <span class="option-number option-number--two">2</span>

  <section class="card card--green">
    <svg class="card__art" viewBox="0 0 418 700" width="418" height="700" aria-hidden="true">
      <defs>
        <radialGradient id="green-glow-top" cx="0.5" cy="0.25" r="0.55">
          <stop offset="0" stop-color="#ffffff"/>
          <stop offset="0.45" stop-color="#e3f3c6"/>
          <stop offset="1" stop-color="#8cc63f"/>
        </radialGradient>
        <radialGradient id="green-glow-bottom" cx="0.5" cy="0.45" r="0.6">
          <stop offset="0" stop-color="#ffffff"/>
          <stop offset="0.4" stop-color="#e6f4cc"/>
          <stop offset="1" stop-color="#8cc63f"/>
        </radialGradient>
        <linearGradient id="orange-swoosh" x1="0" x2="1">
          <stop offset="0" stop-color="#f7941d"/>
          <stop offset="0.5" stop-color="#fff200"/>
          <stop offset="1" stop-color="#f7941d"/>
        </linearGradient>
      </defs>
      <rect width="418" height="700" fill="url(#green-glow-top)"/>
      <path d="M0,330 Q210,420 418,320 L418,700 L0,700 Z" fill="url(#green-glow-bottom)"/>
      <path d="M0,255 Q200,335 418,280 L418,300 Q200,355 0,278 Z" fill="#5fae2e"/>
      <path d="M0,278 Q200,355 418,300 L418,312 Q200,385 0,335 Z" fill="url(#orange-swoosh)"/>
    </svg>
    <div class="pastel-photo" role="img" aria-label="Photo of golden fried pastels stacked together"></div>
    <h1 class="brand-name">Corwin's pastel</h1>
    <p class="phone">
      <svg viewBox="0 0 24 24" aria-hidden="true"><path d="M6.6 10.8a15.1 15.1 0 0 0 6.6 6.6l2.2-2.2a1 1 0 0 1 1-.25 11.4 11.4 0 0 0 3.6.57 1 1 0 0 1 1 1V20a1 1 0 0 1-1 1A17 17 0 0 1 3 4a1 1 0 0 1 1-1h3.5a1 1 0 0 1 1 1c0 1.25.2 2.45.57 3.57a1 1 0 0 1-.25 1z"/></svg>
      <span>0468217094</span>
    </p>
    <p class="email">corwinspastel@fernmail.example</p>
  </section>

  <section class="card card--orange">
    <svg class="card__art" viewBox="0 0 418 700" width="418" height="700" aria-hidden="true">
      <defs>
        <radialGradient id="orange-glow" cx="0.55" cy="0.33" r="0.65">
          <stop offset="0" stop-color="#fff200"/>
          <stop offset="0.35" stop-color="#fcb813"/>
          <stop offset="0.8" stop-color="#f7941d"/>
          <stop offset="1" stop-color="#f15a24"/>
        </radialGradient>
        <radialGradient id="green-glow-lower" cx="0.5" cy="0.45" r="0.6">
          <stop offset="0" stop-color="#ffffff"/>
          <stop offset="0.45" stop-color="#e3f3c6"/>
          <stop offset="1" stop-color="#8cc63f"/>
        </radialGradient>
      </defs>
      <rect width="418" height="700" fill="url(#orange-glow)"/>
      <path d="M0,410 Q220,300 418,400 L418,412 Q220,325 0,430 Z" fill="#2f9a3a"/>
      <path d="M0,430 Q220,325 418,412 L418,425 Q220,345 0,440 Z" fill="#ffffff"/>
      <path d="M0,440 Q220,345 418,425 L418,455 Q220,370 0,455 Z" fill="#f7941d"/>
      <path d="M0,455 Q220,370 418,455 L418,700 L0,700 Z" fill="url(#green-glow-lower)"/>
    </svg>
    <h1 class="brand-name">Corwin's pastel</h1>
    <p class="phone">
      <svg viewBox="0 0 24 24" aria-hidden="true"><path d="M6.6 10.8a15.1 15.1 0 0 0 6.6 6.6l2.2-2.2a1 1 0 0 1 1-.25 11.4 11.4 0 0 0 3.6.57 1 1 0 0 1 1 1V20a1 1 0 0 1-1 1A17 17 0 0 1 3 4a1 1 0 0 1 1-1h3.5a1 1 0 0 1 1 1c0 1.25.2 2.45.57 3.57a1 1 0 0 1-.25 1z"/></svg>
      <span>0468217094</span>
    </p>
    <p class="email">corwinspastel@fernmail.example</p>
    <div class="pastel-photo" role="img" aria-label="Photo of golden fried pastels stacked together"></div>
  </section>
</main>
</body>
</html>
```